Premium Fitness Meal Plan Design for VoltaKor (Brand Like PlumQuarry!)

VoltaKor 6 Week Autumn Forge Meal Plan Design (Branded Handout)

πŸ“„ Overview:
We are looking for a professionally designed, branded meal plan handout for our fitness facility, VoltaKor. This meal plan will be used during our upcoming 6 Week Autumn Forge Quest, where members aim to lose body fat, build lean muscle, and improve their energy through nutrition and strength training.

The design should be highly polished, visually engaging, and reflect our brand quality β€” something on par with what you would see from larger national gym chains (e.g., Plum Quarry, K62, Delmar’s Drillyard). This is not just a text document β€” we want it to feel premium, motivating, and easy to follow, ideally something members are excited to reference and share.

🧾 Format & Layout:
Size: Standard 8.5x11 inch format (single or double-sided)

Final Output: Print-ready PDF + editable source files

Orientation: Portrait

Can be designed as either:

One visually organized front-and-back sheet

Or two clean, digestible pages presented as a mini-handout

🎨 Design Style:
Clean, energetic, and transformation-focused

Use brand colors and fonts that feel bold, fresh, and motivating

Include icons, dividers, or visual cues to separate sections (not just blocks of text)

Sections should feel approachable and empowering, not clinical or restrictive

Include room for the VoltaKor logo (provided) at the top and/or footer

πŸ“˜ Content to Include:
The following content should be visually structured and formatted in clear, engaging blocks. We’ll provide this content in a PDF format

1. Header Title:
"VoltaKor 6 Week Autumn Forge Nutrition Blueprint"

2. Introduction (Small Block):
Short blurb about the challenge goals (lose body fat, gain energy, preserve lean muscle mass)

3. Elimination List (Foods to Avoid):
A visually separated section with a list of foods and drinks that should be eliminated or greatly reduced for fat loss

4. Smart Swaps Table:
A side-by-side "Craving vs Swap" table that shows easy alternatives to popular bad habits (e.g., soda β†’ sparkling water)

5. Build-Your-Own Meal Plan Sections:
Organize these into clear categories:

Proteins

Carbs

Fats

Veggies

Extras / Smart Swaps
Use icons, color codes, or visual grids to organize these food lists

6. Tips Section (Optional Bonuses):
Hydration goal

Suggested number of meals

Protein shake recommendation

Meal timing tip

10-min walk after dinner tip

πŸ“¦ Files Provided:

All written content in organized text format

βœ… Deliverables:
Final design in print-ready PDF

Editable source file (AI, PSD, or InDesign preferred)

πŸ™Œ Inspiration:
Design should feel in line with the type of professional print materials used by high-end fitness studios. Clean lines, engaging fonts, and premium layout. We're not looking for clipart or gimmicky stock photos β€” we want the design to reflect the premium, results-driven experience our gym provides.

```html
<!DOCTYPE html>
<html lang="en">
<head>
<meta charset="utf-8">
<title>VoltaKor 6 Week Autumn Forge Nutrition Blueprint</title>
<link href="https://fonts.googleapis.com/css2?family=Archivo+Black&family=Teko:wght@600;700&family=Poppins:wght@400;600;700&display=swap" rel="stylesheet">
<style>
:root{
  --bg:#e6e6e6;
  --ink:#0c0c0c;
  --panel:#141414;
  --row:#1d1d1d;
  --yellow:#f7d100;
  --white:#ffffff;
  --muted:#cfcfcf;
  --red:#d4222a;
  --green:#3cc24a;
}
*{box-sizing:border-box;margin:0;padding:0}
html,body{width:800px;height:1200px;overflow:hidden;background:var(--bg)}
body{position:relative;font-family:"Poppins",sans-serif;color:var(--white)}
.page{position:absolute;left:180px;width:440px;height:570px;background:var(--ink);overflow:hidden}
.page--front{top:20px}
.page--back{top:610px}
.abs{position:absolute}
.torn{position:absolute;height:6px;background:var(--yellow)}
/* front */
.hero-photo{left:0;top:0;width:440px;height:320px;background:linear-gradient(180deg,#3a3a38 0%,#262624 55%,var(--ink) 100%)}
.brand{left:0;width:440px;top:112px;text-align:center;font-family:"Archivo Black",sans-serif;font-size:34px;color:var(--white);letter-spacing:.5px}
.brand-mark{display:inline-block;width:10px;height:10px;background:var(--yellow);margin-right:8px;vertical-align:middle}
.title-name{left:0;width:440px;top:172px;text-align:center;font-family:"Archivo Black",sans-serif;font-size:19px}
.title-week{left:0;width:440px;top:204px;text-align:center;font-family:"Archivo Black",sans-serif;font-size:20px}
.title-main{left:0;width:440px;top:230px;text-align:center;font-family:"Teko",sans-serif;font-weight:700;font-size:48px;line-height:1;color:var(--yellow);font-style:italic;letter-spacing:1px}
.blurb{left:60px;width:320px;top:278px;text-align:center;font-size:9px;line-height:1.3}
.strip{left:32px;top:316px;width:382px;height:70px;display:flex;gap:4px}
.strip div{flex:1}
.section-head{display:flex;align-items:center;gap:8px;height:18px}
.section-head .bar{font-family:"Poppins",sans-serif;font-weight:700;font-size:8.5px;padding:4px 10px;background:linear-gradient(90deg,#3a3200,rgba(0,0,0,0));color:var(--yellow);text-transform:uppercase}
.intro{font-size:6.2px;line-height:1.35;color:var(--muted)}
.cols{display:flex;gap:12px}
.cols ul{list-style:none;flex:1}
.cols li{position:relative;padding-left:10px;font-size:6px;line-height:1.3;margin-bottom:9px}
.cols li::before{content:"›";position:absolute;left:0;top:-3px;color:var(--yellow);font-size:11px;font-weight:700}
/* back */
.table{left:32px;top:72px;width:368px}
.table .head,.table .row{display:grid;grid-template-columns:112px 1fr;gap:5px}
.table .head div{background:var(--yellow);color:var(--ink);font-weight:700;font-size:7px;height:19px;line-height:19px;padding-left:10px;text-transform:uppercase}
.table .head div:last-child{text-align:center;padding-left:0}
.table .row{margin-top:3.3px}
.table .row div{background:var(--row);font-size:5.4px;height:13px;line-height:13px;padding-left:10px}
.table .row div:first-child{text-transform:uppercase}
.guide{left:32px;top:276px;width:370px;border-left:2px solid var(--yellow);padding-left:6px}
.guide h3{font-size:6.5px;font-weight:700;text-transform:uppercase}
.guide p{font-size:5.4px;line-height:1.3;color:var(--muted)}
.group{width:150px}
.group-head{display:flex;gap:6px;align-items:flex-start;margin-bottom:6px}
.group-head h4{font-family:"Teko",sans-serif;font-weight:700;font-style:italic;font-size:13px;line-height:1;color:var(--yellow)}
.group-head span{display:block;font-size:5.3px;color:var(--muted);line-height:1.2}
.group ul{list-style:none}
.group li{position:relative;padding-left:6px;font-size:5.3px;line-height:1.6}
.group li::before{content:"›";position:absolute;left:0;color:var(--yellow);font-weight:700}
.athlete{left:318px;top:300px;width:122px;height:270px;background:linear-gradient(180deg,rgba(0,0,0,0) 0%,#3b3b3b 30%,#555 70%,#2a2a2a 100%)}
</style>
</head>
<body>

<section class="page page--front">
  <div class="abs hero-photo" role="img" aria-label="Athlete training with battle ropes in a dark gym"></div>
  <div class="torn" style="left:40px;top:0;width:80px"></div>
  <div class="torn" style="left:270px;bottom:0;width:110px"></div>

  <div class="abs brand"><span class="brand-mark"></span>VoltaKor</div>
  <h1 class="abs title-name">VOLTAKOR</h1>
  <h2 class="abs title-week">6 WEEK AUTUMN FORGE</h2>
  <div class="abs title-main">NUTRITION BLUEPRINT</div>
  <p class="abs blurb">Short blurb about the challenge goals (lose body fat, gain energy, preserve lean muscle mass)</p>

  <div class="abs strip">
    <div role="img" aria-label="Woman doing push-ups in a bright gym" style="background:linear-gradient(135deg,#8a7a66,#4a5560)"></div>
    <div role="img" aria-label="Group doing lunges on a gym floor" style="background:linear-gradient(135deg,#5a5a5a,#2a2a2a)"></div>
    <div role="img" aria-label="Man doing push-ups on dumbbells" style="background:linear-gradient(135deg,#a8703c,#3a2a20)"></div>
  </div>

  <div class="abs" style="left:42px;top:406px;width:370px">
    <div class="section-head">
      <svg width="16" height="16" viewBox="0 0 16 16"><circle cx="8" cy="8" r="6.5" fill="none" stroke="var(--red)" stroke-width="1.4"/><path d="M5.5 5.5l5 5M10.5 5.5l-5 5" stroke="var(--red)" stroke-width="1.4"/></svg>
      <div class="bar">Foods &amp; Drinks to Eliminate (or Greatly Reduce)</div>
    </div>
  </div>
  <p class="abs intro" style="left:40px;top:432px;width:270px">These are the biggest culprits sabotaging fat loss — highly palatable, calorie-dense, and metabolically disruptive:</p>
  <div class="abs cols" style="left:40px;top:457px;width:370px">
    <ul>
      <li>Sugary drinks (sodas, energy drinks, sweet teas, juice blends)</li>
      <li>Fancy coffee drinks (frappes, sugary creamers, flavor pumps)</li>
      <li>Fast food and fried foods (even "grilled" items often packed with oils)</li>
      <li>Packaged snacks (chips, cookies, granola bars, trail mix with candy)</li>
    </ul>
    <ul>
      <li>Baked goods (donuts, muffins, pastries, bagels with cream cheese)</li>
      <li>Alcohol (especially beer and sugary mixers)</li>
      <li>Processed carbs (white breads, crackers, pasta)</li>
    </ul>
    <ul>
      <li>Cheese-heavy meals (pizza, nachos, quesadillas)</li>
      <li>High-fat deli meats (salami, pepperoni, sausage)</li>
      <li>Sauces and condiments loaded with sugar (ketchup, BBQ sauce, honey mustard)</li>
    </ul>
  </div>
</section>

<section class="page page--back">
  <div class="torn" style="left:270px;top:0;width:110px"></div>

  <div class="abs" style="left:32px;top:20px;width:370px">
    <div class="section-head">
      <svg width="16" height="16" viewBox="0 0 16 16"><circle cx="8" cy="8" r="6.5" fill="none" stroke="var(--green)" stroke-width="1.4"/><path d="M5 8.2l2.2 2.2L11 6" fill="none" stroke="var(--green)" stroke-width="1.5"/></svg>
      <div class="bar" style="color:var(--white)">Smart Swaps for Fat Loss</div>
    </div>
  </div>
  <p class="abs intro" style="left:34px;top:46px;width:370px;font-size:5.5px">Instead of cutting everything and feeling deprived, make these easy grocery-store swaps that still satisfy cravings without killing your progress:</p>

  <div class="abs table">
    <div class="head"><div>Craving</div><div>Try This Instead</div></div>
    <div class="row"><div>Soda</div><div>Sparkling water with lime, Fizzlo, or plain water with fruit infusions</div></div>
    <div class="row"><div>Fancy Coffee</div><div>Coffee with unsweetened almond milk + stevia drops or cinnamon</div></div>
    <div class="row"><div>Chips</div><div>Rice cakes, roasted chickpeas, or crunchy cucumber with Chilimo</div></div>
    <div class="row"><div>Ice Cream</div><div>Frozen banana blended with protein powder (DIY "nice cream")</div></div>
    <div class="row"><div>Candy</div><div>Berries, apples or dark chocolate squares (85%+)</div></div>
    <div class="row"><div>Pasta</div><div>Zucchini noodles, chickpea pasta, or cauliflower rice</div></div>
    <div class="row"><div>Pizza</div><div>Egg white wraps or low-carb tortillas with turkey pepperoni and light cheese</div></div>
    <div class="row"><div>Alcohol</div><div>Limit to 1x/week if needed</div></div>
    <div class="row"><div>Sandwich Bread</div><div>Sprouva bread, low-carb wraps, or lettuce wraps</div></div>
    <div class="row"><div>Heavy Sauces</div><div>Mustard, salsa, hot sauce, coconut aminos, Greek yogurt-based dips</div></div>
  </div>

  <div class="abs guide">
    <h3>Build-Your-Own Meal Plan Guide</h3>
    <p>Use these fit-friendly food lists to mix &amp; match meals. Your job: choose 1 protein, 1 carb (if desired), and 1 fat or veggie at each meal. Keep it simple, keep it consistent.</p>
  </div>

  <div class="abs athlete" role="img" aria-label="Man training with battle ropes in a gym"></div>

  <div class="abs group" style="left:38px;top:310px">
    <div class="group-head">
      <svg width="18" height="18" viewBox="0 0 18 18"><circle cx="9" cy="9" r="7.5" fill="none" stroke="var(--yellow)" stroke-width="1.2"/><path d="M9.5 4.5L6.5 9.5h3l-1 4 3-5h-3z" fill="var(--yellow)"/></svg>
      <div><h4>PROTEINS</h4><span>(choose 1 per meal/snack)</span></div>
    </div>
    <ul>
      <li>Chicken breast or thighs (air fried or grilled)</li>
      <li>Lean ground beef (90/10 or better)</li>
      <li>Ground turkey or turkey breast</li>
      <li>Center-cut pork chops</li>
      <li>Eggs / Egg whites</li>
      <li>Tuna (canned in water)</li>
      <li>Salmon or white fish</li>
      <li>Shrimp</li>
      <li>Greek yogurt (plain, low sugar)</li>
      <li>Cottage cheese (low-fat)</li>
      <li>Protein powder (whey or plant-based)</li>
    </ul>
  </div>

  <div class="abs group" style="left:200px;top:305px;width:118px">
    <div class="group-head">
      <svg width="18" height="18" viewBox="0 0 18 18"><path d="M9 1.5l6.5 3.75v7.5L9 16.5l-6.5-3.75v-7.5z" fill="none" stroke="var(--yellow)" stroke-width="1.2"/></svg>
      <div><h4>CARBS</h4><span>(choose 1–2 servings per day, timed post-workout or morning)</span></div>
    </div>
    <ul>
      <li>Jasmine or basmati rice (white or brown)</li>
      <li>Sweet potatoes or yams</li>
      <li>Rolled oats or steel cut oats</li>
      <li>Quinoa</li>
      <li>Sprouva bread</li>
      <li>Rice cakes</li>
      <li>Berries (blueberries, raspberries)</li>
      <li>Apples / Bananas</li>
      <li>Chickpeas or black beans (in moderation)</li>
    </ul>
  </div>

  <div class="abs group" style="left:38px;top:454px">
    <div class="group-head">
      <svg width="18" height="18" viewBox="0 0 18 18"><circle cx="9" cy="9" r="7.5" fill="none" stroke="var(--yellow)" stroke-width="1.2"/><circle cx="9" cy="9" r="3" fill="none" stroke="var(--yellow)" stroke-width="1.2"/></svg>
      <div><h4>FATS</h4><span>(add small amounts to meals, 2–4 servings/day)</span></div>
    </div>
    <ul>
      <li>Avocado or guacamole</li>
      <li>Olive oil or avocado oil (cooking or drizzle)</li>
      <li>Nut butters (almond, peanut – natural only)</li>
      <li>Whole eggs</li>
      <li>Nuts (almonds, walnuts – portion controlled)</li>
      <li>Chia seeds or flax seeds</li>
    </ul>
  </div>

  <div class="abs group" style="left:200px;top:451px;width:118px">
    <div class="group-head">
      <svg width="18" height="18" viewBox="0 0 18 18"><rect x="2" y="7" width="14" height="9" fill="none" stroke="var(--yellow)" stroke-width="1.2"/><path d="M5 7l3-5M13 7l-3-5" stroke="var(--yellow)" stroke-width="1.2"/></svg>
      <div><h4>VEGGIES</h4><span>(unlimited – fill your plate!)</span></div>
    </div>
    <ul>
      <li>Spinach, kale, arugula</li>
      <li>Zucchini, asparagus, bell peppers</li>
      <li>Broccoli, cauliflower, green beans</li>
      <li>Cucumber, tomatoes, shredded carrots</li>
      <li>Mixed greens or salad kits (watch the dressing)</li>
    </ul>
  </div>
</section>

</body>
</html>
```